Photography Business Card Design

I want a simple,classy design using a logo and simple font such as minion pro or similar. I have attached a logo that I quite like or am open to something similar. On the back of the card I would like the attached photo possibly with my website address on it some where. I want a matt black with silver or grey print. Possibly have the logo off to one side with the words Daniel Festerby Photography stacked on top of each other
Updates
I am very sorry that some how I forgot to put my facebook address on the details section, www.socialpage.example/DanielFesterbyPhotography
If this could be include on the card as well.
Industry/Entity Type
Business
Contact Information for Business Card
Daniel Festerby Photography
www.danielfesterbyphotography.example.au
Email: danielfesterby@wirenest.example
Phone: +61 (0)427 318 502
Logo Text
Logo styles of interest
Abstract Logo
Look and feel

```html
<!DOCTYPE html>
<html lang="en">
<head>
<meta charset="utf-8">
<title>Daniel Festerby Photography – Business Card Artwork</title>
<link rel="stylesheet" href="https://fonts.googleapis.com/css2?family=Crimson+Text&family=Oswald:wght@500&family=Arimo:wght@400;700&display=swap">
<style>
  :root {
    --board: #c3c3c3;
    --ink: #111111;
    --card-white: #ffffff;
    --card-black: #000000;
    --print-grey: #3a3a3a;
    --rule: #7a7a7a;
    --light-text: #f2f2f2;
    --photo-warm: #7a6240;
    --photo-mid: #4a4a46;
    --photo-dark: #000000;
  }
  html, body {
    margin: 0;
    padding: 0;
    overflow: hidden;
  }
  body {
    width: 1200px;
    height: 458px;
    background: var(--board);
    position: relative;
    font-family: "Arimo", Arial, sans-serif;
  }
  .board-title {
    position: absolute;
    left: 10px;
    top: 4px;
    margin: 0;
    font-family: "Oswald", "Arial Narrow", sans-serif;
    font-weight: 500;
    font-size: 38px;
    line-height: 1;
    letter-spacing: 4px;
    color: var(--ink);
  }
  .side-label {
    position: absolute;
    top: 394px;
    font-family: "Oswald", "Arial Narrow", sans-serif;
    font-weight: 500;
    font-size: 22px;
    letter-spacing: 3px;
    color: var(--ink);
  }
  .side-label--back { left: 456px; }
  .side-label--front { left: 990px; }

  .card {
    position: absolute;
    top: 77px;
    height: 304px;
    overflow: hidden;
  }
  .card--back {
    left: 54px;
    width: 536px;
    background: var(--card-white);
    color: var(--print-grey);
  }
  .card--front {
    left: 608px;
    width: 590px;
    background: var(--card-black);
    color: var(--light-text);
  }

  .wordmark {
    position: absolute;
    white-space: nowrap;
  }
  .wordmark__name {
    display: block;
    font-family: "Crimson Text", "Minion Pro", Georgia, serif;
    line-height: 1;
  }
  .wordmark__trade {
    display: block;
    font-family: "Arimo", Arial, sans-serif;
    font-weight: 700;
    font-size: 12px;
    letter-spacing: 3px;
  }
  .card--back .wordmark { left: 72px; top: 82px; color: var(--ink); }
  .card--back .wordmark__name { font-size: 45px; letter-spacing: 3px; }
  .card--back .wordmark__trade { margin: 4px 0 0 188px; color: var(--print-grey); }
  .card--front .wordmark { left: 72px; top: 114px; z-index: 1; }
  .card--front .wordmark__name { font-size: 42px; letter-spacing: 3px; }
  .card--front .wordmark__trade { margin: 4px 0 0 178px; }

  .contact-rule {
    position: absolute;
    left: 29px;
    top: 217px;
    width: 460px;
    height: 0;
    border-top: 1px solid var(--rule);
  }
  .contact-web {
    position: absolute;
    left: 0;
    width: 536px;
    top: 228px;
    text-align: center;
    font-size: 13px;
  }
  .contact-row {
    position: absolute;
    top: 255px;
    font-size: 13px;
    display: flex;
    align-items: center;
    gap: 6px;
    white-space: nowrap;
  }
  .contact-row--email { left: 38px; }
  .contact-row--phone { left: 320px; }
  .contact-row svg { display: block; }

  .photo-montage {
    position: absolute;
    left: 0;
    top: 0;
  }
</style>
</head>
<body>
  <h1 class="board-title">ARTWORK - PHOTOGRAPHY BUSINESS CARD V1</h1>

  <section class="card card--back" aria-label="Back side of business card">
    <div class="wordmark">
      <span class="wordmark__name">Daniel Festerby</span>
      <span class="wordmark__trade">PHOTOGRAPHY</span>
    </div>
    <div class="contact-rule"></div>
    <div class="contact-web">www.danielfesterbyphotography.example.au</div>
    <div class="contact-row contact-row--email">
      <svg width="16" height="12" viewBox="0 0 16 12" aria-hidden="true">
        <rect x="0.75" y="0.75" width="14.5" height="10.5" fill="none" stroke="#3a3a3a" stroke-width="1.5"/>
        <path d="M1 1 L8 7 L15 1" fill="none" stroke="#3a3a3a" stroke-width="1.5"/>
      </svg>
      <span>: danielfesterby@wirenest.example</span>
    </div>
    <div class="contact-row contact-row--phone">
      <svg width="10" height="16" viewBox="0 0 10 16" aria-hidden="true">
        <rect x="0.75" y="0.75" width="8.5" height="14.5" rx="1.5" fill="none" stroke="#3a3a3a" stroke-width="1.5"/>
        <rect x="2.5" y="3" width="5" height="7" fill="#3a3a3a"/>
      </svg>
      <span>: +61 (0)427 318 502</span>
    </div>
  </section>

  <section class="card card--front" aria-label="Front side of business card">
    <svg class="photo-montage" width="590" height="304" viewBox="0 0 590 304" role="img" aria-label="Montage of the photographer's work">
      <defs>
        <radialGradient id="montage-tones" cx="430" cy="152" r="230" gradientUnits="userSpaceOnUse">
          <stop offset="0" stop-color="#7a6240"/>
          <stop offset="0.5" stop-color="#4a4a46"/>
          <stop offset="1" stop-color="#000000"/>
        </radialGradient>
      </defs>
      <rect width="590" height="304" fill="url(#montage-tones)"/>
    </svg>
    <div class="wordmark">
      <span class="wordmark__name">Daniel Festerby</span>
      <span class="wordmark__trade">PHOTOGRAPHY</span>
    </div>
  </section>

  <span class="side-label side-label--back">BACK SIDE</span>
  <span class="side-label side-label--front">FRONT SIDE</span>
</body>
</html>
```